Contemporary Elegant Business Card Design for an International Trade Company in the Wine Industry

We need a new business card design for an international trade company in the wine and winemaking industry. The overall feel of the card should be contemporary, upscale, luxurious and elegant. It should communicate confidence and professionalism. The colors should complementary to our logo design (burgundy, gold, and black).
Inspiration: rich velvet tapestry
The card should include the following information:
Business: Brovenna Trading/Shipping, LLC.
Name: Marcus T. Hollenbrand
Title: CEO
Email: mark@brovennatrading.example
Phone: 555-294-6172
www.brovennatrading.example
Updates
Project Deadline Extended
Reason: We'd like the designers that we requested some additional designs from to still submit designs. Thank you!
Industry/Entity Type
Business
Contact Information for Business Card
Title: CEO
Phone: 555-294-6172
www.brovennatrading.example
Look and feel

```html
<!DOCTYPE html>
<html lang="en">
<head>
<meta charset="utf-8">
<title>Brovenna Trading/Shipping, LLC. — Business Card</title>
<link rel="stylesheet" href="https://fonts.googleapis.com/css2?family=Arimo:wght@400;700&family=Lato:wght@400;700&display=swap">
<style>
  :root {
    --page: #e4e4e6;
    --burgundy: #7a1622;
    --burgundy-deep: #5a0d17;
    --gold: #d99a2b;
    --gold-light: #f3cf7a;
    --gold-dark: #b5771c;
    --ink: #0e0e0e;
    --ink-soft: #1c1c1c;
    --paper: #f6f6f4;
    --text-light: #f2f2f2;
    --map-tan: #c98a3a;
    --map-brown: #8a5420;
  }
  * { box-sizing: border-box; margin: 0; padding: 0; }
  html, body { width: 1200px; height: 900px; overflow: hidden; }
  body {
    background: var(--page);
    font-family: "Lato", Arial, sans-serif;
    position: relative;
  }

  .card {
    position: absolute;
    left: 280px;
    width: 640px;
    height: 366px;
    border-radius: 20px;
    padding: 14px;
    background: linear-gradient(170deg, var(--burgundy) 0%, var(--burgundy) 35%, #a8401f 60%, var(--gold) 85%);
    box-shadow: 0 10px 28px rgba(0,0,0,0.22);
  }
  .card--front { top: 48px; }
  .card--back  { top: 486px; }

  .card__face {
    position: relative;
    width: 100%;
    height: 100%;
    border-radius: 14px;
    background: var(--ink);
    overflow: hidden;
  }

  .world-map {
    position: absolute;
    inset: 0;
    background:
      radial-gradient(ellipse 30% 40% at 25% 45%, var(--ink-soft), transparent 70%),
      radial-gradient(ellipse 35% 45% at 70% 40%, var(--ink-soft), transparent 70%);
  }

  .company-name {
    font-family: "Arimo", Arial, sans-serif;
    font-weight: 700;
    text-transform: uppercase;
    background: linear-gradient(180deg, var(--gold-light) 0%, var(--gold) 55%, var(--gold-dark) 100%);
    -webkit-background-clip: text;
    background-clip: text;
    color: transparent;
    line-height: 1;
  }

  /* Front */
  .front__brand { position: absolute; left: 34px; top: 30px; }
  .front__brand .company-name--main { font-size: 50px; letter-spacing: 1px; }
  .front__brand .company-name--sub  { font-size: 19px; letter-spacing: 0.5px; margin-top: 4px; }

  .contact { position: absolute; left: 34px; top: 150px; }
  .contact__name { color: var(--gold); font-size: 21px; }
  .contact__title { color: var(--text-light); font-size: 12px; margin-top: 2px; margin-bottom: 8px; }
  .contact__line {
    display: flex; align-items: center; gap: 8px;
    color: var(--text-light); font-size: 14px; line-height: 22px;
  }
  .contact__icon { width: 13px; height: 13px; flex: none; }

  .brand-panel {
    position: absolute;
    right: 18px; bottom: -10px;
    width: 290px; height: 184px;
    background: var(--paper);
    border-radius: 14px;
    padding: 14px 14px 0 14px;
  }
  .brand-panel__art { display: flex; height: 96px; }
  .brand-panel__field { width: 50%; background: var(--burgundy); }
  .brand-panel__map {
    width: 50%;
    background: radial-gradient(ellipse at 45% 40%, var(--map-tan), var(--map-brown));
  }
  .brand-panel__mark {
    display: flex; align-items: center; gap: 10px;
    margin-top: 10px;
  }
  .brand-panel__square { width: 18px; height: 18px; background: var(--burgundy); flex: none; }
  .brand-panel__words { display: flex; flex-direction: column; gap: 3px; }
  .brand-panel__name {
    font-family: "Arimo", Arial, sans-serif;
    font-weight: 700;
    font-size: 26px;
    line-height: 1;
    letter-spacing: 1px;
    color: var(--ink);
    text-transform: uppercase;
    white-space: nowrap;
  }
  .brand-panel__sub {
    font-family: "Arimo", Arial, sans-serif;
    font-weight: 700;
    font-size: 10px;
    line-height: 1.1;
    letter-spacing: 1px;
    color: var(--ink);
    text-transform: uppercase;
    white-space: nowrap;
  }

  /* Back */
  .back__brand {
    position: absolute; left: 0; right: 0; top: 100px;
    text-align: center;
  }
  .back__brand .company-name--main { font-size: 74px; letter-spacing: 2px; }
  .back__brand .company-name--sub  { font-size: 26px; letter-spacing: 1px; margin-top: 6px; }
  .back__url {
    position: absolute; left: 0; right: 0; top: 262px;
    text-align: center;
    color: var(--text-light);
    font-size: 13px; letter-spacing: 1.5px; text-transform: uppercase;
  }
</style>
</head>
<body>

<section class="card card--front">
  <div class="card__face">
    <div class="world-map" role="img" aria-label="Faint dark world map in the background"></div>

    <div class="front__brand">
      <div class="company-name company-name--main">Brovenna</div>
      <div class="company-name company-name--sub">Trading/Shipping, LLC.</div>
    </div>

    <div class="contact">
      <div class="contact__name">Marcus T. Hollenbrand</div>
      <div class="contact__title">CEO</div>
      <div class="contact__line">
        <svg class="contact__icon" viewBox="0 0 16 16"><rect x="1" y="1" width="14" height="14" rx="2" fill="var(--gold)"/><path d="M5 4c1 0 1.5 2 1 2.5L5.5 7c.6 1.4 1.8 2.6 3.5 3.4l.6-.6c.5-.5 2.5 0 2.5 1 0 .8-1 1.7-2 1.7C6.5 12.5 3.5 9.5 3.5 5.8 3.5 4.8 4.2 4 5 4z" fill="var(--ink)"/></svg>
        <span>555-294-6172</span>
      </div>
      <div class="contact__line">
        <svg class="contact__icon" viewBox="0 0 16 16"><rect x="1" y="1" width="14" height="14" rx="2" fill="var(--gold)"/><rect x="3.5" y="5" width="9" height="6.5" fill="none" stroke="var(--ink)" stroke-width="1.2"/><path d="M3.5 5l4.5 3.5L12.5 5" fill="none" stroke="var(--ink)" stroke-width="1.2"/></svg>
        <span>mark@brovennatrading.example</span>
      </div>
      <div class="contact__line">
        <svg class="contact__icon" viewBox="0 0 16 16"><rect x="1.5" y="2.5" width="13" height="9" rx="1" fill="none" stroke="var(--gold)" stroke-width="1.5"/><rect x="6" y="12" width="4" height="2" fill="var(--gold)"/></svg>
        <span>www.brovennatrading.example</span>
      </div>
    </div>

    <div class="brand-panel">
      <div class="brand-panel__art">
        <div class="brand-panel__field"></div>
        <div class="brand-panel__map" role="img" aria-label="Antique parchment-toned map of Europe and Africa"></div>
      </div>
      <div class="brand-panel__mark">
        <span class="brand-panel__square"></span>
        <span class="brand-panel__words">
          <span class="brand-panel__name">Brovenna</span>
          <span class="brand-panel__sub">Trading/Shipping</span>
        </span>
      </div>
    </div>
  </div>
</section>

<section class="card card--back">
  <div class="card__face">
    <div class="world-map" role="img" aria-label="Faint dark world map in the background"></div>
    <div class="back__brand">
      <div class="company-name company-name--main">Brovenna</div>
      <div class="company-name company-name--sub">Trading/Shipping, LLC.</div>
    </div>
    <div class="back__url">www.brovennatrading.example</div>
  </div>
</section>

</body>
</html>
```